New Karvenna Business Cards with new logo

Need to keep the Logo of the guys in the boat, or new logo with guys in a boat that symbolizes the three different Alaska natives that represent the region. Would like to have in font "An Alaska Village Corporation". Business cards should include logo, and be professional. knri.com is the company website that we are looking at redesigning also.

Target Market(s)

Business Contact

Industry/Entity Type

Business

Contact Information for Business Card

Would like Name, title, address, two phone numbers Cell and direct, email.

Logo Text

Logo does not have to have text,

Font styles to use
Serif
Sans Serif

Colors

Designer to choose colors to be used in the design.

Requirements
Must have
• An Alaska Native Village Corporation; Karvenna Heritage Collective Inc. (company name)

```html
<!DOCTYPE html>
<html lang="en">
<head>
<meta charset="utf-8">
<title>Karvenna Heritage Collective – Business Cards</title>
<link rel="stylesheet" href="https://fonts.googleapis.com/css2?family=Libre+Baskerville:wght@700&family=Open+Sans:wght@400;600&display=swap">
<style>
  :root {
    --backdrop: #3b3431;
    --card: #1c1d1f;
    --card-edge: #141516;
    --emboss: #8d8f93;
    --text: #f2f2f2;
    --muted: #9a9ca0;
    --accent: #3c58a8;
    --divider: #cfd3d8;
  }
  * { box-sizing: border-box; margin: 0; padding: 0; }
  html, body { width: 1200px; height: 864px; overflow: hidden; }
  body {
    background: var(--backdrop);
    font-family: "Open Sans", sans-serif;
    position: relative;
  }
  .card {
    position: absolute;
    width: 540px;
    height: 309px;
    background: var(--card);
    border: 1px solid var(--card-edge);
    border-radius: 3px;
    box-shadow: 0 10px 24px rgba(0,0,0,.45);
  }
  .card--front { left: 40px; top: 110px; }
  .card--back { left: 620px; top: 420px; }

  /* front */
  .front__mark {
    position: absolute;
    left: 0; right: 0; top: 92px;
    text-align: center;
    font-family: "Libre Baskerville", serif;
    font-weight: 700;
    font-size: 19px;
    letter-spacing: 1px;
    line-height: 1.35;
    color: var(--emboss);
    text-transform: uppercase;
  }
  .front__web {
    position: absolute;
    left: 0; right: 0; top: 222px;
    text-align: center;
    font-size: 14px;
    letter-spacing: 7px;
    color: var(--muted);
  }

  /* back */
  .back__mark {
    position: absolute;
    left: 28px; top: 118px;
    width: 210px;
    display: flex;
    align-items: center;
    gap: 10px;
    font-family: "Open Sans", sans-serif;
    font-weight: 600;
    font-size: 13px;
    line-height: 1.3;
    color: var(--text);
  }
  .back__mark-dot {
    flex: none;
    width: 14px; height: 14px;
    border-radius: 50%;
    background: var(--accent);
  }
  .back__divider {
    position: absolute;
    left: 262px; top: 40px;
    width: 2px; height: 230px;
    background: linear-gradient(to bottom, transparent, var(--divider) 45%, transparent);
  }
  .back__details {
    position: absolute;
    left: 284px; top: 48px;
    color: var(--text);
    font-size: 13px;
    line-height: 1.32;
  }
  .back__name {
    color: var(--accent);
    font-weight: 600;
    text-transform: uppercase;
    font-size: 13.5px;
  }
  .back__title { text-transform: uppercase; font-size: 14px; margin-bottom: 8px; }
  .back__address { margin-bottom: 4px; }
  .contact { display: flex; align-items: center; gap: 8px; }
  .contact svg { width: 11px; height: 11px; flex: none; fill: var(--accent); }
</style>
</head>
<body>

<section class="card card--front" aria-label="Business card front">
  <div class="front__mark">Karvenna Heritage<br>Collective Inc.</div>
  <div class="front__web">www.knri.com</div>
</section>

<section class="card card--back" aria-label="Business card back">
  <div class="back__mark">
    <span class="back__mark-dot"></span>
    <span>Karvenna Heritage Collective Inc.</span>
  </div>
  <div class="back__divider"></div>
  <div class="back__details">
    <div class="back__name">Ellis Marrow</div>
    <div class="back__title">CEO/Founder</div>
    <div class="back__address">An Alaska Native Village Corporation<br>4120 Tundra Ridge Road<br>Anchorage, Alaska 99515</div>
    <div class="contact">
      <svg viewBox="0 0 12 12" aria-hidden="true"><path d="M2 1h2.5l1 3-1.5 1a6 6 0 0 0 3 3l1-1.5 3 1V10a1 1 0 0 1-1 1A9 9 0 0 1 1 2a1 1 0 0 1 1-1z"/></svg>
      <span>907 555 0142</span>
    </div>
    <div class="contact">
      <svg viewBox="0 0 12 12" aria-hidden="true"><path d="M3 0h6a1 1 0 0 1 1 1v10a1 1 0 0 1-1 1H3a1 1 0 0 1-1-1V1a1 1 0 0 1 1-1zm0 2v7h6V2zm3 8a.6.6 0 1 0 0 1.2.6.6 0 0 0 0-1.2z"/></svg>
      <span>907 555 0187</span>
    </div>
    <div class="contact">
      <svg viewBox="0 0 12 12" aria-hidden="true"><path d="M3 0h5v3H3zM1 4h10v5H9v3H3V9H1zm3 4v3h4V8z"/></svg>
      <span>907 555 0123</span>
    </div>
    <div class="contact">
      <svg viewBox="0 0 12 12" aria-hidden="true"><path d="M0 2h12v1L6 7 0 3zm0 2.2 6 4 6-4V10H0z"/></svg>
      <span>name@knri.com</span>
    </div>
    <div class="contact">
      <svg viewBox="0 0 12 12" aria-hidden="true"><circle cx="6" cy="6" r="5.5"/></svg>
      <span>www.knri.com</span>
    </div>
  </div>
</section>

</body>
</html>
```